Business Card Design Project

I need a business card design for my freelance solo makeup artistry business in Melbourne, Australia called Rosa Marindi. My freelance business specialises in bridal and special occassions makeup.

I like the idea of having Rosa Marindi in pink as its a feminine and soft colour. I would like a very clean, classy and simple (with an element of fun if that's possible) design. I would consider the business name to be in gloss with an otherwise matte finish.

Underneath the business name, I would like "Makeup by Tessa Colwick"

I do not want any bridal related graphics.

Target Market(s)

Young females with a disposable income from ages 20-40 and females getting married who will dictate who does mother of bride makeup ages 40-70.

Industry/Entity Type

Business

Requirements
Must have
• "Makeup by Tessa Colwick"

Ph: 0412 385 604
E: rosamarindi@inboxly.net
ABN: 58204917362
Nice to have
• I think I would like a mini business cards which is more slimline. I do like the colours of pink, white and grey but open to suggestions.
Should not have
• Bridal related graphics

```html
<!DOCTYPE html>
<html lang="en">
<head>
<meta charset="utf-8">
<title>Rosa Marindi – Business Card</title>
<link rel="stylesheet" href="https://fonts.googleapis.com/css2?family=Courgette&family=Arimo:wght@400;700&display=swap">
<style>
  :root {
    --page-bg: #3a3a3c;
    --card-pink: #e5007d;
    --card-pink-deep: #c8006c;
    --gloss: #f9cfe5;
    --contact: #f6d9e8;
  }
  html, body {
    margin: 0;
    width: 1200px;
    height: 900px;
    overflow: hidden;
    background: var(--page-bg);
  }
  .sheet {
    position: relative;
    width: 1200px;
    height: 900px;
  }
  .card {
    position: absolute;
    width: 600px;
    height: 366px;
    background: linear-gradient(135deg, var(--card-pink) 0%, var(--card-pink) 55%, var(--card-pink-deep) 100%);
    box-shadow: 0 10px 30px rgba(0,0,0,0.45);
    box-sizing: border-box;
  }
  .card--front { left: 300px; top: 44px; }
  .card--back  { left: 300px; top: 490px; }

  .brand {
    font-family: "Courgette", cursive;
    color: var(--gloss);
    line-height: 1.1;
  }
  .brand p { margin: 0; }
  .brand__name { font-size: 58px; }
  .brand__rule {
    height: 2px;
    background: var(--gloss);
    border: 0;
    margin: 6px 4% 8px;
  }
  .brand__tagline { font-size: 26px; }

  .card--front .brand {
    position: absolute;
    left: 50%;
    top: 50%;
    transform: translate(-50%, -50%);
    text-align: center;
    white-space: nowrap;
  }

  .card--back .brand {
    position: absolute;
    left: 34px;
    top: 28px;
    white-space: nowrap;
  }
  .card--back .brand__name { font-size: 36px; }
  .card--back .brand__rule { margin: 4px 8% 5px 0; height: 1.5px; }
  .card--back .brand__tagline { font-size: 17px; }

  .holder {
    position: absolute;
    left: 60px;
    right: 0;
    top: 165px;
    text-align: center;
    font-family: "Courgette", cursive;
    font-size: 30px;
    line-height: 1.1;
    color: var(--gloss);
    margin: 0;
  }

  .contact {
    position: absolute;
    right: 40px;
    bottom: 30px;
    margin: 0;
    font-family: "Arimo", Arial, sans-serif;
    font-size: 16px;
    letter-spacing: 2px;
    line-height: 1.5;
    color: var(--contact);
  }
  .contact__label { font-weight: 700; }
</style>
</head>
<body>
<main class="sheet">
  <section class="card card--front" aria-label="Card front">
    <div class="brand">
      <p class="brand__name">Rosa Marindi</p>
      <hr class="brand__rule">
      <p class="brand__tagline">Makeup by Tessa Colwick</p>
    </div>
  </section>

  <section class="card card--back" aria-label="Card back">
    <div class="brand">
      <p class="brand__name">Rosa Marindi</p>
      <hr class="brand__rule">
      <p class="brand__tagline">Makeup by Tessa Colwick</p>
    </div>
    <p class="holder">Tessa Colwick</p>
    <p class="contact">
      <span class="contact__label">Ph:</span> 0412 385 604<br>
      <span class="contact__label">E:</span> rosamarindi@inboxly.net<br>
      <span class="contact__label">ABN:</span> 58204917362
    </p>
  </section>
</main>
</body>
</html>
```